LET ME HANDLE YOUR AUCTION NEEDS!

I am here to handle all your auction needs, I have over 20 years of auction experience buying and selling for dealerships in North Carolina and Tennessee. Send me to the sale to either rep your vehicles or let me know what you need and I can be
another set of eyes to help you buy what is hot and bad credit cars are my specialty. You know a car always sells better with a familiar face rather than auction personnel and with my great reputation I will be able to help find the buyers for your aged inventory.
Call me today and let's get started.
Rick Halvorsen 555-862-3917
(please have pictures of vehicles or an auto auction in the design)

```html
<!DOCTYPE html>
<html lang="en">
<head>
<meta charset="utf-8">
<title>Let Me Handle Your Auction Needs</title>
<link rel="stylesheet" href="https://fonts.googleapis.com/css2?family=Open+Sans:wght@400;600;700&family=Roboto+Condensed:wght@700&family=Roboto:wght@400&display=swap">
<style>
  :root {
    --page-bg: #e6e6e6;
    --card-white: #ffffff;
    --title-blue: #1e88e5;
    --panel-blue-light: #2f9bef;
    --panel-blue-dark: #1565c0;
    --accent-orange: #f7a81b;
    --wave-gray: #4a4a4a;
    --ink-dark: #222222;
    --bar-dark: #1c1c1c;
    --bar-mid: #3b3b3b;
    --text-white: #ffffff;
  }
  html, body {
    margin: 0;
    padding: 0;
    width: 1200px;
    height: 1056px;
    overflow: hidden;
    background: var(--page-bg);
  }
  .flyer {
    position: absolute;
    left: 30px;
    top: 118px;
    width: 1140px;
    height: 820px;
    background: var(--card-white);
    overflow: hidden;
    box-shadow: 0 4px 14px rgba(0,0,0,0.18);
  }
  .flyer__waves {
    position: absolute;
    inset: 0;
    width: 1140px;
    height: 820px;
  }
  .flyer__photo {
    position: absolute;
    left: 686px;
    top: 76px;
    width: 624px;
    height: 624px;
    border-radius: 50%;
    box-sizing: border-box;
    border: 10px solid var(--accent-orange);
    box-shadow: 0 0 0 16px var(--card-white), 0 0 0 26px var(--wave-gray);
    background:
      radial-gradient(ellipse 60% 35% at 55% 58%, #fbfbfb 0%, #e9ecef 60%, rgba(233,236,239,0) 100%),
      linear-gradient(160deg, #c9ced3 0%, #e7e9eb 45%, #b9bec4 100%);
  }
  .flyer__headline {
    position: absolute;
    left: 51px;
    top: 42px;
    margin: 0;
  }
  .headline__main {
    display: block;
    font-family: "Roboto Condensed", "Arial Narrow", sans-serif;
    font-weight: 700;
    font-size: 72px;
    line-height: 1;
    color: var(--title-blue);
    letter-spacing: 0.5px;
  }
  .headline__sub {
    display: block;
    margin-top: 14px;
    font-family: "Roboto", Arial, sans-serif;
    font-weight: 400;
    font-size: 38px;
    line-height: 1;
    color: var(--ink-dark);
    letter-spacing: 0.5px;
  }
  .flyer__body {
    position: absolute;
    left: 51px;
    top: 318px;
    width: 612px;
    margin: 0;
    font-family: "Open Sans", Arial, sans-serif;
    font-size: 23.5px;
    line-height: 31.5px;
    color: var(--text-white);
    text-align: justify;
  }
  .flyer__body .highlight {
    color: var(--accent-orange);
    font-weight: 700;
  }
  .flyer__contact-bar {
    position: absolute;
    left: 0;
    top: 711px;
    width: 1140px;
    height: 109px;
    background: linear-gradient(90deg, var(--bar-dark) 0%, var(--bar-mid) 55%, var(--bar-dark) 100%);
    z-index: 2;
  }
  .contact-bar__cta {
    position: absolute;
    left: 46px;
    top: 34px;
    font-family: "Roboto Condensed", "Arial Narrow", sans-serif;
    font-weight: 700;
    font-size: 33px;
    line-height: 1;
    color: var(--accent-orange);
  }
  .contact-bar__divider {
    position: absolute;
    left: 559px;
    top: 18px;
    width: 2px;
    height: 74px;
    background: var(--text-white);
  }
  .contact-bar__details {
    position: absolute;
    left: 578px;
    top: 14px;
    font-family: "Open Sans", Arial, sans-serif;
  }
  .contact-bar__name {
    display: block;
    font-weight: 700;
    font-size: 37px;
    line-height: 42px;
    color: var(--accent-orange);
  }
  .contact-bar__phone {
    display: block;
    font-weight: 600;
    font-size: 32px;
    line-height: 38px;
    color: var(--text-white);
  }
</style>
</head>
<body>
  <div class="flyer">
    <svg class="flyer__waves" viewBox="0 0 628 452" aria-hidden="true">
      <defs>
        <linearGradient id="panelBlue" x1="0" y1="0" x2="1" y2="1">
          <stop offset="0" stop-color="var(--panel-blue-light)"/>
          <stop offset="0.55" stop-color="#2a8ee6"/>
          <stop offset="1" stop-color="var(--panel-blue-dark)"/>
        </linearGradient>
      </defs>
      <path class="wave-gray" d="M0,98 C120,150 270,128 420,62 L470,62 L470,388 L0,388 Z" fill="var(--wave-gray)"/>
      <path class="wave-white" d="M0,106 C120,158 270,136 420,70 L470,70 L470,388 L0,388 Z" fill="var(--card-white)"/>
      <path class="wave-orange" d="M0,110 C120,162 270,140 420,74 L470,74 L470,388 L0,388 Z" fill="var(--accent-orange)"/>
      <path class="wave-panel" d="M0,116 C120,168 270,146 420,80 L470,80 L470,388 L0,388 Z" fill="url(#panelBlue)"/>
    </svg>

    <div class="flyer__photo" role="img" aria-label="Photo of a white sports car parked in a bright showroom"></div>

    <h1 class="flyer__headline">
      <span class="headline__main">LET ME HANDLE</span>
      <span class="headline__sub">YOUR AUCTION NEEDS</span>
    </h1>

    <p class="flyer__body">I am here to handle all your auction needs, I have over <span class="highlight">20 years</span> of auction experience buying and selling for dealerships in North Carolina and Tennessee. Send me to the sale to either rep your vehicles or let me know what you need and I can be another set of eyes to help you buy what is hot and bad credit cars are my specialty. You know a car always sells better with a familiar face rather than auction personnel and with my great reputation I will be able to help find the buyers for your aged inventory.</p>

    <div class="flyer__contact-bar">
      <span class="contact-bar__cta">Call me today and let's get started</span>
      <span class="contact-bar__divider"></span>
      <div class="contact-bar__details">
        <span class="contact-bar__name">Rick Halvorsen</span>
        <span class="contact-bar__phone">555-862-3917</span>
      </div>
    </div>
  </div>
</body>
</html>
```